The best Social Research house in LatinAmerica needs a Business Card

We need a greeting card that does justice to our everyday work. Lumentra Civica is a group of highly selected social academic minds (6 academicians selected among 800+ candidates) that analyses the field work done by our network of 56 social anthropologists in 7 Latin American countries. We spend months studying different social phenomena or groups of people and then translate the findings into powerful insights and strategic marketing actions for our clients (from Banks to TV networks, from top worldwide consumer product Companies to Government policy design or even new product innovation initiatives). We translate social academic knowledge into tangible actions. We already have a logo and we like it, but remain open for new and different proposals on size or form. We do something very different and we need a card as different as we are.
Target Market(s)
Top Management from Top Companies that need (and like) to be surprised!
Industry/Entity Type
Marketing
Look and feel

```html
<!DOCTYPE html>
<html lang="es">
<head>
<meta charset="utf-8">
<title>Lumentra Civica — Tarjeta de presentación</title>
<link rel="stylesheet" href="https://fonts.googleapis.com/css2?family=Arvo:wght@400;700&display=swap">
<style>
  :root {
    --page-bg: #e9e7e3;
    --brand-teal: #0c8f72;
    --brand-teal-deep: #0a7d63;
    --brand-green: #6bb936;
    --card-white: #ffffff;
    --card-white-shade: #f1f1f1;
    --ink: #3b3b3b;
    --ink-soft: #4a4a4a;
    --faint-shape: #e3e5e4;
  }
  * { box-sizing: border-box; margin: 0; padding: 0; }
  html, body {
    width: 1200px;
    height: 900px;
    overflow: hidden;
    background: var(--page-bg);
    font-family: "Arvo", Georgia, serif;
  }
  .canvas {
    position: relative;
    width: 1200px;
    height: 900px;
    display: flex;
    flex-direction: column;
    align-items: center;
    justify-content: center;
    gap: 44px;
  }
  .card {
    position: relative;
    width: 630px;
    height: 360px;
    border-radius: 3px;
    overflow: hidden;
    box-shadow: 0 10px 26px rgba(0, 0, 0, 0.18);
  }

  /* Front */
  .card-front {
    background: linear-gradient(160deg, var(--brand-teal) 0%, var(--brand-teal-deep) 100%);
    display: flex;
    align-items: center;
    justify-content: center;
  }
  .front-accent {
    position: absolute;
    right: -70px;
    top: -70px;
    width: 240px;
    height: 240px;
    border-radius: 50%;
    background: rgba(255, 255, 255, 0.05);
  }
  .wordmark {
    display: flex;
    align-items: center;
    gap: 18px;
  }
  .wordmark-dot {
    width: 46px;
    height: 46px;
    border-radius: 50%;
    background: var(--card-white);
  }
  .wordmark-name {
    font-weight: 700;
    font-size: 46px;
    letter-spacing: -0.5px;
    color: var(--card-white);
  }

  /* Back */
  .card-back {
    background: linear-gradient(180deg, var(--card-white) 0%, var(--card-white-shade) 100%);
  }
  .back-accent {
    position: absolute;
    right: -90px;
    top: 60px;
    width: 280px;
    height: 280px;
    border-radius: 50%;
    background: var(--faint-shape);
  }
  .person {
    position: absolute;
    left: 52px;
    top: 52px;
  }
  .person-name {
    font-size: 27px;
    font-weight: 400;
    color: var(--ink);
    letter-spacing: 0.3px;
  }
  .person-role {
    margin-top: 2px;
    font-size: 15px;
    color: var(--ink-soft);
    letter-spacing: 0.6px;
  }
  .contact-list {
    position: absolute;
    left: 52px;
    top: 190px;
    list-style: none;
    display: flex;
    flex-direction: column;
    gap: 12px;
  }
  .contact-item {
    display: flex;
    align-items: flex-start;
    gap: 12px;
    font-size: 15px;
    line-height: 20px;
    color: var(--ink);
  }
  .contact-icon {
    flex: none;
    width: 22px;
    height: 22px;
    border-radius: 50%;
    background: var(--brand-green);
    display: flex;
    align-items: center;
    justify-content: center;
  }
  .contact-icon svg { width: 13px; height: 13px; }
</style>
</head>
<body>
  <main class="canvas">
    <section class="card card-front" aria-label="Frente de la tarjeta">
      <div class="front-accent"></div>
      <div class="wordmark">
        <span class="wordmark-dot"></span>
        <span class="wordmark-name">Lumentra Civica</span>
      </div>
    </section>

    <section class="card card-back" aria-label="Reverso de la tarjeta">
      <div class="back-accent"></div>
      <div class="person">
        <h1 class="person-name">Tomás Rivera</h1>
        <p class="person-role">Gabinete de Análisis</p>
      </div>
      <ul class="contact-list">
        <li class="contact-item">
          <span class="contact-icon">
            <svg viewBox="0 0 24 24" fill="#fff"><path d="M6.6 10.8a15.1 15.1 0 0 0 6.6 6.6l2.2-2.2a1 1 0 0 1 1-.25 11.4 11.4 0 0 0 3.6.57 1 1 0 0 1 1 1V20a1 1 0 0 1-1 1A17 17 0 0 1 3 4a1 1 0 0 1 1-1h3.5a1 1 0 0 1 1 1c0 1.25.2 2.45.57 3.57a1 1 0 0 1-.25 1z"/></svg>
          </span>
          <span>(55) 5550 1234</span>
        </li>
        <li class="contact-item">
          <span class="contact-icon">
            <svg viewBox="0 0 24 24" fill="none" stroke="#fff" stroke-width="2.4"><rect x="3" y="5" width="18" height="14" rx="1"/><path d="M3 6l9 7 9-7"/></svg>
          </span>
          <span>tomas.rivera@lumentra-civica.com</span>
        </li>
        <li class="contact-item">
          <span class="contact-icon">
            <svg viewBox="0 0 24 24" fill="#fff"><path d="M12 2a7 7 0 0 0-7 7c0 5.2 7 13 7 13s7-7.8 7-13a7 7 0 0 0-7-7zm0 9.5A2.5 2.5 0 1 1 12 6.5a2.5 2.5 0 0 1 0 5z"/></svg>
          </span>
          <span>Calle Olmo 14. Col. Roma<br>Mexico DF 06700. MX.</span>
        </li>
      </ul>
    </section>
  </main>
</body>
</html>
```